Computer consultant website

Vexlo Software is a newly started computer consulting company. It's a small one-man company that provides mostly Android applications but also websites in collaboration with designers. I'm running this company on the side of full time university studies.

I'm in need of a website which will function as:
Primarily - I'll direct potential clients to the page so they can read about the company, what i offer and past work.
Secondarily - Making my company visible through the web and maybe getting new clients.

The final design should look modern, clean and professional.

Pages that will be in the final website are (Note that it's not the exact titles as the page will not be in english):
* About
* Services (what Vexlo offers)
* Portfolio/work
* Short news (like PlanHives "News and press")
* Contact.

Inspiration
http://www.planhive.example/design/87836
http://www.brambleorb.example/
http://www.planhive.example/design/845881
http://www.planhive.example/design/1369424 - Lighter design, however a bit cluttered.

No programming code is needed delivered at all. Focus on designing rather then coding.

If you have any questions, do not hesitate to send me a message.

Target Market(s)

Non-technical entrepreneurs and small companies.

Industry/Entity Type

University

Requirements
Must have
• Must have my company logo (see attachment).

Must in any way use both colors from my logo.

A way to logically rearrange content to fit smaller screens. I will implement this design so that it can be pleasantly viewed on mobile devices. You don't necessarily need to provide exactly how the design would look on mobile devices.

I need the following types of page designs:
* Landing page
* Content page
* Portfolio/work (with accompanying inside/clicked) page

Landing/start page must in any way include at least the information:
* Shorter version of "About Vexlo"
* At least 1 most recent portfolio/work entry
* At least 1 most recent news entry
* Services that Vexlo offers.
Nice to have
Should not have
• Testimonials or newsletter.

```html
<!DOCTYPE html>
<html lang="en">
<head>
<meta charset="utf-8">
<title>Vexlo Software</title>
<link rel="stylesheet" href="https://fonts.googleapis.com/css2?family=Cabin:wght@400;500;600&display=swap">
<style>
:root{
  --header-bg:#2b3236;
  --nav-bg:#1d2124;
  --nav-border:#34393c;
  --accent:#1f6fe6;
  --accent-text:#2a6fd6;
  --about-bg:#e3e7ee;
  --dark-bg:#323b3f;
  --card-bg:#fafbfc;
  --panel-bg:#262b2e;
  --footer-bg:#e2e2e2;
  --ink:#2b2f33;
  --ink-soft:#3a3f44;
  --light:#e9ecef;
  --green:#6fae3a;
}
*{margin:0;padding:0;box-sizing:border-box}
html,body{width:1003px;height:1200px;overflow:hidden}
body{font-family:"Cabin",Arial,sans-serif;color:var(--ink);background:var(--footer-bg);position:relative}

.site-header{position:absolute;left:0;top:0;width:1003px;height:89px;background:radial-gradient(ellipse at 20% 40%,#4a555b 0%,var(--header-bg) 60%)}
.brand{position:absolute;left:155px;top:22px;display:flex;align-items:center;gap:10px}
.brand-dot{width:34px;height:34px;border-radius:50%;background:var(--accent)}
.brand-name{font-size:38px;font-weight:600;color:#3a4247;letter-spacing:-1px}
.main-nav{position:absolute;left:493px;top:0;display:flex;height:89px}
.main-nav a{display:flex;align-items:center;justify-content:center;height:89px;background:var(--nav-bg);border-right:1px solid var(--nav-border);color:#e6e8ea;text-decoration:none;font-size:14px}
.main-nav a.active{background:linear-gradient(#2a7df2,#1557d4);color:#fff}

.hero{position:absolute;left:0;top:89px;width:1003px;height:356px;background:radial-gradient(ellipse at 50% 30%,#f5f5f5 0%,#dcdcdc 70%,#c9c9c9 100%)}
.hero-photo{position:absolute;left:120px;top:8px;width:820px;height:348px;background:linear-gradient(90deg,rgba(130,140,170,.35),rgba(235,200,220,.45) 50%,rgba(170,205,230,.4))}
.hero-caption{position:absolute;left:138px;top:183px;width:730px;height:91px;background:rgba(255,255,255,.35);padding:14px 0 0 35px}
.hero-caption h1{font-weight:400;font-size:28px;color:#333;line-height:1.1}
.hero-caption p{font-size:21px;color:#333;line-height:1.2}
.hero-rule{position:absolute;left:0;top:445px;width:1003px;height:8px;background:#cfd2d6}

.about{position:absolute;left:0;top:453px;width:1003px;height:258px;background:var(--about-bg)}
.about-title{position:absolute;left:157px;top:57px;display:flex;align-items:center;gap:9px;font-weight:400;font-size:20px;color:var(--ink)}
.about-title .dot{width:30px;height:30px;border-radius:50%;background:var(--accent)}
.about-text{position:absolute;left:157px;top:102px;width:349px;font-size:10.3px;line-height:15.4px;color:var(--ink-soft);text-align:justify}
.latest-title{position:absolute;left:578px;top:43px;font-weight:400;font-size:16.5px;color:var(--ink)}
.latest-frame{position:absolute;left:571px;top:79px;width:294px;height:153px;background:#c4c7cb;padding:7px}
.latest-shot{width:100%;height:100%;background:linear-gradient(90deg,#f4f4f4 0 24%,#6b6b6b 24% 100%)}

.services{position:absolute;left:0;top:711px;width:1003px;height:372px;background:var(--dark-bg)}
.service-card{position:absolute;top:16px;width:232px;height:127px;background:var(--card-bg);overflow:hidden}
.service-card h2{position:absolute;left:61px;top:14px;font-weight:400;font-size:18.5px;color:var(--accent-text)}
.service-card p{position:absolute;left:31px;top:50px;width:190px;font-size:13.3px;line-height:15.5px;color:var(--ink-soft)}
.service-card svg.icon{position:absolute;left:19px;top:13px}
.service-card .more{position:absolute;right:0;bottom:0}

.news{position:absolute;left:139px;top:173px;width:355px;height:155px;background:var(--panel-bg);color:var(--light)}
.news-thumb{position:absolute;left:7px;top:9px;width:66px;height:57px;background:linear-gradient(135deg,#2d4a66,#7a8fa5 60%,#c99e82)}
.news-label{position:absolute;left:81px;top:15px;font-size:10.5px}
.news-label span{color:#4b8ff0}
.news-more{position:absolute;left:295px;top:15px;font-size:9px;color:var(--green)}
.news-line{position:absolute;left:294px;top:29px;width:52px;height:1px;background:#444a4e}
.news h3{position:absolute;left:81px;top:29px;font-weight:400;font-size:18px;color:#f0f2f4}
.news-date{position:absolute;left:81px;top:53px;font-size:8px;color:#d0d4d8}
.news-body{position:absolute;left:8px;top:74px;width:342px;font-size:9.5px;line-height:12.5px;color:#e3e6e9}
.pager{position:absolute;display:flex;gap:1px}
.pager span{width:16px;height:16px;background:#e8eaec;display:flex;align-items:center;justify-content:center}
.news .pager{left:8px;top:128px}

.portfolio-thumb{position:absolute;top:173px;width:113px;height:114px}
.portfolio-label{position:absolute;left:726px;top:303px;display:flex;align-items:center;gap:8px;font-size:17px;color:var(--light)}
.portfolio-label .dot{width:20px;height:20px;border-radius:50%;background:var(--accent)}
.services .pager.portfolio{left:829px;top:303px}

.site-footer{position:absolute;left:0;top:1083px;width:1003px;height:117px;background:var(--footer-bg)}
.footer-brand{position:absolute;left:140px;top:40px;display:flex;align-items:center;gap:6px}
.footer-brand .dot{width:20px;height:20px;border-radius:50%;background:#1b1e20}
.footer-brand .name{font-size:19px;font-weight:600;color:#1b1e20}
.footer-brand small{font-size:8.5px;color:#222;margin-left:4px}
</style>
</head>
<body>

<header class="site-header">
  <div class="brand"><span class="brand-dot"></span><span class="brand-name">Vexlo</span></div>
  <nav class="main-nav">
    <a href="#" style="width:61px">About</a>
    <a href="#" style="width:73px">Services</a>
    <a href="#" class="active" style="width:78px">Portfolio</a>
    <a href="#" style="width:89px">Short news</a>
    <a href="#" style="width:78px">Contact</a>
  </nav>
</header>

<section class="hero">
  <div class="hero-photo" role="img" aria-label="Three colleagues in office clothes working with laptops"></div>
  <div class="hero-caption">
    <h1>Headline,</h1>
    <p>Tagline for call to action.</p>
  </div>
</section>
<div class="hero-rule"></div>

<section class="about">
  <h2 class="about-title"><span class="dot"></span>About Vexlo</h2>
  <p class="about-text">Lorem ipsum dolor sit amet, consectetur adipiscing elit. Maecenas quis rhoncus nibh. Quisque facilisis nisl vitae enim mattis id vehicula est commodo. Duis venenatis volutpat congue. Morbi eu nisl odio, tincidunt viverra tortor. Vestibulum sagittis malesuada lectus, non faucibus neque placerat ac. Nullam quis congue est. Suspendisse at commodo elit. Nulla sit amet turpis vitae nulla dictum vulputate.</p>
  <h2 class="latest-title">Latest work</h2>
  <div class="latest-frame">
    <div class="latest-shot" role="img" aria-label="Screenshot of a recent client website with a furniture showroom photo"></div>
  </div>
</section>

<section class="services">
  <article class="service-card" style="left:138px">
    <svg class="icon" width="28" height="26" viewBox="0 0 28 26"><rect x="1" y="1" width="26" height="17" fill="none" stroke="#2a2f33" stroke-width="2.5"/><rect x="11" y="18" width="6" height="4" fill="#2a2f33"/><rect x="6" y="22" width="16" height="2.5" fill="#2a2f33"/></svg>
    <h2>Service one</h2>
    <p>Lorem ipsum dolor sit amet, consectetur adipiscing elit. Maecenas quis</p>
    <svg class="more" width="44" height="44" viewBox="0 0 44 44"><polygon points="44,0 44,44 0,44" fill="#2c3235"/><path d="M32 25v12M26 31h12" stroke="#e6e8ea" stroke-width="3.5"/></svg>
  </article>
  <article class="service-card" style="left:385px">
    <svg class="icon" width="28" height="28" viewBox="0 0 28 28"><g transform="rotate(45 14 14)"><rect x="8" y="6" width="12" height="12" rx="2" fill="#2a2f33"/><rect x="10" y="0" width="2.5" height="7" fill="#2a2f33"/><rect x="15.5" y="0" width="2.5" height="7" fill="#2a2f33"/><rect x="12.5" y="18" width="3" height="10" fill="#2a2f33"/></g></svg>
    <h2>Service two</h2>
    <p>Lorem ipsum dolor sit amet, consectetur adipiscing elit.</p>
    <svg class="more" width="44" height="44" viewBox="0 0 44 44"><polygon points="44,0 44,44 0,44" fill="#2c3235"/><path d="M32 25v12M26 31h12" stroke="#e6e8ea" stroke-width="3.5"/></svg>
  </article>
  <article class="service-card" style="left:633px">
    <svg class="icon" width="28" height="28" viewBox="0 0 28 28"><ellipse cx="14" cy="17" rx="8" ry="9" fill="#2a2f33"/><circle cx="14" cy="6" r="4" fill="#2a2f33"/><path d="M6 12L1 9M6 17H0M6 22l-5 3M22 12l5-3M22 17h6M22 22l5 3" stroke="#2a2f33" stroke-width="2"/></svg>
    <h2>Service three</h2>
    <p>Lorem ipsum dolor sit amet, consectetur adipiscing elit. Maecenas quis rhoncus nibh.</p>
    <svg class="more" width="44" height="44" viewBox="0 0 44 44"><polygon points="44,0 44,44 0,44" fill="#2c3235"/><path d="M32 25v12M26 31h12" stroke="#e6e8ea" stroke-width="3.5"/></svg>
  </article>

  <article class="news">
    <div class="news-thumb" role="img" aria-label="Small preview of a newly launched website"></div>
    <div class="news-label">Recent <span>News</span></div>
    <div class="news-more">read more</div>
    <div class="news-line"></div>
    <h3>New website lounched.</h3>
    <div class="news-date">☰ &nbsp;29.03.2013</div>
    <p class="news-body">Lorem ipsum dolor sit amet, consectetur adipiscing elit. Aenean eu augue in elit imperdiet rhoncus eget a lacus. Aenean gravida egestas augue volutpat dictum. Pellentesque et lectus turpis. Etiam nulla justo, tincidunt et placerat vitae, bibendum at arcu. Aliquam erat volutpat. Phasellus a dignissim lacus. Nam et</p>
    <div class="pager">
      <span><svg width="8" height="10" viewBox="0 0 8 10"><path d="M6 1L2 5l4 4" fill="none" stroke="#222" stroke-width="1.6"/></svg></span>
      <span><svg width="8" height="10" viewBox="0 0 8 10"><path d="M2 1l4 4-4 4" fill="none" stroke="#222" stroke-width="1.6"/></svg></span>
    </div>
  </article>

  <div class="portfolio-thumb" style="left:515px;background:linear-gradient(#1a1a1a,#3a3a3a 50%,#151515)" role="img" aria-label="Dark themed website screenshot"></div>
  <div class="portfolio-thumb" style="left:633px;background:linear-gradient(90deg,#e8e3da,#b9b2a6 50%,#e8e3da)" role="img" aria-label="Online shop website screenshot with product grid"></div>
  <div class="portfolio-thumb" style="left:751px;background:linear-gradient(90deg,#f2f2f2 0 25%,#6b5b5b 25% 100%)" role="img" aria-label="Music store website screenshot with album grid"></div>

  <div class="portfolio-label"><span class="dot"></span>Portfolio</div>
  <div class="pager portfolio">
    <span><svg width="8" height="10" viewBox="0 0 8 10"><path d="M6 1L2 5l4 4" fill="none" stroke="#222" stroke-width="1.6"/></svg></span>
    <span><svg width="8" height="10" viewBox="0 0 8 10"><path d="M2 1l4 4-4 4" fill="none" stroke="#222" stroke-width="1.6"/></svg></span>
  </div>
</section>

<footer class="site-footer">
  <div class="footer-brand"><span class="dot"></span><span class="name">Vexlo</span><small>2013. All rights reserved</small></div>
</footer>

</body>
</html>
```